Fahrzeugbeschriftung für Varno Telmio 2012 Kasten
Zielgruppe
Werbetechnik aller Art, siehe www.wendolux.de
Aufgabenstellung
Es wird ein pfiffiges Design gesucht. Eine Vollverklebung ist nicht möglich, größere Flächen allerdings schon. Gerne auch mit Werbegesicht, also nicht so langweilig wie die bisherige Beklebung.
www.wendolux.de

```html
<!DOCTYPE html>
<html lang="de">
<head>
<meta charset="utf-8">
<title>Wendolux – Heckbeschriftung</title>
<link rel="stylesheet" href="https://fonts.googleapis.com/css2?family=Fira+Sans+Condensed:wght@500;600;700&display=swap">
<style>
  :root {
    --orange: #e67817;
    --grey: #6b6b6b;
    --white: #ffffff;
    --ink: #1d1d1d;
    --stage: #e9e9e9;
    --photo-a: #d9a27f;
    --photo-b: #6e4530;
  }
  html, body {
    margin: 0;
    padding: 0;
    width: 1157px;
    height: 1200px;
    overflow: hidden;
    background: var(--stage);
  }
  .rear-panel {
    display: block;
    width: 1157px;
    height: 1200px;
    font-family: "Fira Sans Condensed", "Arial Narrow", sans-serif;
  }
  .panel-base { fill: var(--white); }
  .field-orange { fill: var(--orange); }
  .band-grey { fill: var(--grey); }
  .band-white { fill: var(--white); }
  .arc-grey { fill: none; stroke: var(--grey); stroke-width: 16; }
  .arc-white { fill: none; stroke: var(--white); stroke-width: 8; }
  .brand-name { fill: #2a2a2a; font-weight: 600; font-size: 66px; letter-spacing: -1px; }
  .service { fill: var(--ink); font-weight: 700; font-size: 17px; letter-spacing: 0.3px; }
  .tick { fill: none; stroke: var(--orange); stroke-width: 2.6; stroke-linecap: round; stroke-linejoin: round; }
  .slogan { fill: var(--orange); font-weight: 700; font-size: 21px; }
  .web { fill: var(--white); font-weight: 700; font-size: 30px; }
  .phone { fill: var(--white); font-weight: 700; font-size: 23px; }
  .address { fill: var(--orange); font-weight: 700; font-size: 19px; }
</style>
</head>
<body>
<svg class="rear-panel" viewBox="0 0 1000 1037" xmlns="http://www.w3.org/2000/svg" aria-label="Heckbeschriftung Wendolux">
  <defs>
    <clipPath id="panel-shape">
      <path d="M150 42 H850 Q893 42 893 85 V860 Q893 875 878 875 H122 Q105 875 105 860 V85 Q105 42 150 42 Z"/>
    </clipPath>
    <linearGradient id="photo-tone" x1="0" y1="0" x2="0" y2="1">
      <stop offset="0" stop-color="var(--photo-a)"/>
      <stop offset="1" stop-color="var(--photo-b)"/>
    </linearGradient>
  </defs>

  <g clip-path="url(#panel-shape)">
    <rect class="panel-base" x="100" y="40" width="800" height="840"/>

    <!-- orange main field -->
    <path class="field-orange" d="M150 40 H900 V700 C700 640 400 570 150 555 Z"/>

    <!-- top-left corner bands -->
    <polygon class="band-white" points="100,40 215,40 100,250"/>
    <polygon class="band-grey" points="100,250 215,40 262,40 100,330"/>
    <polygon class="band-white" points="100,330 262,40 280,40 100,365"/>

    <!-- right white arc field -->
    <path class="band-white" d="M515 40 C480 250 550 425 705 474 S 860 500 900 500 V40 Z"/>
    <path class="arc-white" d="M491 40 C456 256 526 444 693 496 S 860 520 900 520"/>
    <path class="arc-grey" d="M504 40 C469 250 539 432 700 483 S 860 507 900 507"/>

    <!-- lower swooshes -->
    <path class="band-white" d="M100 552 C350 560 650 620 900 700 V745 C650 660 380 600 100 590 Z"/>
    <path class="band-grey" d="M160 585 C420 600 680 660 900 745 V795 C700 700 420 625 160 605 Z"/>
    <path class="band-white" d="M100 600 C420 625 700 700 900 795 V880 H100 Z"/>

    <!-- advertising face photo -->
    <rect x="190" y="40" width="248" height="385" rx="60" fill="url(#photo-tone)" role="img" aria-label="Foto: Frau kopfüber mit Händen am Gesicht, überraschter Ausdruck"/>
  </g>

  <text class="brand-name" x="560" y="190">Wendolux</text>

  <g class="services">
    <path class="tick" d="M586 243 l5 5 l9 -9"/>
    <text class="service" x="607" y="251">DIGITALE MEDIEN</text>
    <path class="tick" d="M586 267 l5 5 l9 -9"/>
    <text class="service" x="607" y="275">DRUCK + VEREDELUNG</text>
    <path class="tick" d="M586 291 l5 5 l9 -9"/>
    <text class="service" x="607" y="299">WERBETECHNIK</text>
  </g>

  <g class="slogan-block">
    <text class="slogan" x="613" y="340">Werbung kann jeder,</text>
    <text class="slogan" x="613" y="369">aber wir können es</text>
    <text class="slogan" x="613" y="398">einfach besser!</text>
  </g>

  <text class="web" x="210" y="497">www.wendolux.de</text>
  <text class="phone" x="190" y="530">Phone 07120-558314-0</text>

  <text class="address" x="542" y="763">Lindenweg 14</text>
  <text class="address" x="542" y="790">72100 halderbach</text>
</svg>
</body>
</html>
```